Business Card for Lawyer

I'm looking for a business card for my new law firm, based in Ontario, Canada. I would prefer single sided. I am partial (but not limited) to white and blue color wise and like things understated. Also, if you can work in the red QK rating symbol from Presworth-Calloway, that would be a plus.

Target Market(s)

Old people - so it should be easy to read.

Industry/Entity Type

Business

Contact Information for Business Card

See the specs in the word document below. Also, see the design for my website. The card should have a similar look to the site.

Requirements
Must have
• Everything listed in the business card specs. I don't mind having the address set off at the bottom of the card on its own line.
Should not have
• 1) Any sort of design that could also be used by a tattoo parlour or a tarot card reader, mystic etc.
• 2) There should not be any photographs of me (or anyone else).

```html
<!DOCTYPE html>
<html lang="en">
<head>
<meta charset="utf-8">
<title>Whitmore Law Firm – Business Card</title>
<link rel="stylesheet" href="https://fonts.googleapis.com/css2?family=Open+Sans:wght@400;600;700&display=swap">
<style>
  :root {
    --brand-blue: #0a78c0;
    --brand-red: #b8392a;
    --ink: #151515;
    --paper: #ffffff;
    --backdrop: #e6e8eb;
    --badge-grey: #8c8f91;
    --badge-light: #d9dadb;
  }
  html, body {
    margin: 0;
    padding: 0;
    width: 1200px;
    height: 1200px;
    overflow: hidden;
    background: var(--backdrop);
    font-family: "Open Sans", Arial, sans-serif;
    color: var(--ink);
  }
  .canvas { position: relative; width: 1200px; height: 1200px; }
  .card {
    position: absolute;
    left: 109px;
    width: 969px;
    background: var(--paper);
    box-shadow: 0 4px 14px rgba(0,0,0,.18);
    overflow: hidden;
  }
  .card--front { top: 16px; height: 566px; }
  .card--back { top: 612px; height: 562px; }
  .card-shapes { position: absolute; inset: 0; }

  .firm-mark {
    position: absolute;
    border-radius: 50%;
    background: var(--brand-red);
  }
  .firm-name {
    position: absolute;
    margin: 0;
    text-align: center;
    font-weight: 600;
    color: var(--ink);
    line-height: 1.05;
    letter-spacing: .5px;
  }
  .firm-tagline {
    position: absolute;
    margin: 0;
    text-align: center;
    color: #222;
  }

  /* front */
  .card--front .firm-mark { left: 153px; top: 80px; width: 164px; height: 164px; }
  .card--front .firm-name { left: 0; width: 478px; top: 262px; font-size: 48px; }
  .card--front .firm-tagline { left: 0; width: 478px; top: 366px; font-size: 19px; }
  .divider {
    position: absolute; left: 445px; top: 89px; width: 2px; height: 277px;
    background: #333;
  }
  .contact { position: absolute; left: 497px; top: 94px; }
  .contact-name { margin: 0; font-size: 41px; font-weight: 400; line-height: 1.2; }
  .contact-credentials { margin: 0; font-size: 24px; font-weight: 600; color: var(--brand-red); line-height: 1.3; }
  .contact-address { margin: 14px 0 6px; font-size: 24px; line-height: 35px; color: #222; }
  .contact-line { display: flex; align-items: center; gap: 10px; font-size: 24px; height: 40px; color: #222; }
  .contact-line svg { width: 24px; height: 24px; }

  .web-links { position: absolute; left: 42px; top: 458px; color: #fff; }
  .web-link { display: flex; align-items: center; gap: 20px; font-size: 24px; font-weight: 600; height: 46px; }
  .web-link svg { width: 30px; height: 30px; }

  .rating-badge { position: absolute; left: 688px; top: 470px; width: 250px; height: 74px; }

  /* back */
  .card--back .firm-mark { left: 376px; top: 57px; width: 210px; height: 210px; }
  .card--back .firm-name { left: 0; width: 969px; top: 262px; font-size: 64px; }
  .card--back .firm-tagline { left: 0; width: 969px; top: 400px; font-size: 25px; }
  .practice-areas {
    position: absolute; left: 0; width: 969px; top: 505px; margin: 0;
    text-align: center; font-size: 21px; letter-spacing: .3px; color: #222;
  }
  .practice-areas .sep { margin: 0 6px; color: #444; }
</style>
</head>
<body>
<main class="canvas">

  <section class="card card--front" aria-label="Card front">
    <svg class="card-shapes" width="969" height="566" viewBox="0 0 969 566" aria-hidden="true">
      <defs>
        <linearGradient id="badgeField" x1="0" y1="0" x2="1" y2="0">
          <stop offset="0" stop-color="#ffffff"/>
          <stop offset="1" stop-color="#eeeeee"/>
        </linearGradient>
      </defs>
      <polygon points="0,20 403,20 440,0 969,0 969,37 0,37" fill="var(--brand-blue)"/>
      <rect x="0" y="432" width="969" height="134" fill="url(#badgeField)"/>
      <rect x="0" y="432" width="969" height="14" fill="var(--brand-blue)"/>
      <polygon points="0,446 581,446 668,566 0,566" fill="var(--brand-blue)"/>
    </svg>

    <div class="firm-mark" aria-hidden="true"></div>
    <p class="firm-name">WHITMORE<br>LAW FIRM</p>
    <p class="firm-tagline">Getting the results that matter</p>

    <div class="divider"></div>

    <div class="contact">
      <h1 class="contact-name">Daniel R. Whitmore</h1>
      <p class="contact-credentials">B.A. &amp; J.D.</p>
      <p class="contact-address">1 Harbour Lane East, Ground Floor,<br>Kingsford, ON K7P 2X4</p>
      <div class="contact-line">
        <svg viewBox="0 0 24 24" aria-label="Phone"><rect width="24" height="24" rx="4" fill="var(--brand-red)"/><path d="M8 5c1 0 1.5 2.5 1.5 3.3 0 .8-1.3 1-1.1 2 .5 1.8 1.8 3.3 3.4 4 .9.3 1.3-1 2-1 .9 0 3.2.6 3.2 1.6 0 1.4-1.5 3-3 3-4.4-.3-8.5-4.7-8.7-9.2C5.3 6.4 6.8 5 8 5z" fill="#fff"/></svg>
        <span>555-013-0234</span>
      </div>
      <div class="contact-line">
        <svg viewBox="0 0 24 24" aria-label="Fax"><rect width="24" height="24" rx="4" fill="var(--brand-red)"/><rect x="5" y="10" width="14" height="8" rx="1.5" fill="#fff"/><rect x="8" y="5" width="8" height="5" fill="#fff"/><rect x="8" y="13" width="8" height="1.5" fill="var(--brand-red)"/></svg>
        <span>555.014.1234</span>
      </div>
    </div>

    <div class="web-links">
      <div class="web-link">
        <svg viewBox="0 0 30 30" aria-label="Website"><g fill="none" stroke="#fff" stroke-width="2"><circle cx="15" cy="15" r="12"/><ellipse cx="15" cy="15" rx="5.5" ry="12"/><line x1="3" y1="15" x2="27" y2="15"/><path d="M5 9h20M5 21h20"/></g></svg>
        <span>www.whitmorefirm.ca</span>
      </div>
      <div class="web-link">
        <svg viewBox="0 0 30 30" aria-label="Email"><g fill="none" stroke="#fff" stroke-width="2"><rect x="3" y="7" width="24" height="16"/><path d="M3 7l12 10 12-10M3 23l9-8M27 23l-9-8"/></g></svg>
        <span>email@whitmorefirm.ca</span>
      </div>
    </div>

    <svg class="rating-badge" viewBox="0 0 250 74" role="img" aria-label="Peer review rating badge">
      <circle cx="30" cy="36" r="28" fill="var(--badge-grey)"/>
      <rect x="66" y="22" width="180" height="28" fill="var(--badge-light)"/>
    </svg>
  </section>

  <section class="card card--back" aria-label="Card back">
    <div class="firm-mark" aria-hidden="true"></div>
    <p class="firm-name">WHITMORE<br>LAW FIRM</p>
    <p class="firm-tagline">Getting the results that matter</p>
    <p class="practice-areas">Barrister<span class="sep">|</span>Solicitor &amp; Notary Public<span class="sep">|</span>Trial Lawyer<span class="sep">|</span>Lawyer<span class="sep">|</span>Litigation Counsel</p>
  </section>

</main>
</body>
</html>
```